Torvale Works- Plumbing Business Card

We need a business card design for a new company that services Canberra and surrounds. We are a professional family-owned plumbing company who has 20+ years' experience. We would like to use our logo as well as the colours black, white, grey and the signature green. The final design needs to communicate professional, high-end, plumbing with reliable service. We provide obligation free quotes and are open 24/7. Services include: Bathroom/kitchen renovations, drainage, stormwater, water leaks, plumbing maintenance, water tanks and septics.

Target Market(s)

Homeowners, real estate agents, builders, small business owners

Industry/Entity Type

Plumbing & Construction

Font styles to use
Serif
Sans Serif

Colors
59FF00
82FF00
B8FF75
E3FFCB
F4FFEA

Requirements
Must have
• Must have logo, example of services and contact details

```html
<!DOCTYPE html>
<html lang="en">
<head>
<meta charset="utf-8">
<title>Torvale Works – Business Card</title>
<link href="https://fonts.googleapis.com/css2?family=Fira+Sans:wght@400;600&family=Montserrat:wght@800&display=swap" rel="stylesheet">
<style>
  :root {
    --green: #17a54b;
    --charcoal: #3a3a3c;
    --ink: #333335;
    --white: #ffffff;
    --page: #fdfdfd;
  }
  * { margin: 0; padding: 0; box-sizing: border-box; }
  html, body { width: 1009px; height: 1200px; overflow: hidden; background: var(--page); }
  .canvas { position: relative; width: 1009px; height: 1200px; }

  .card {
    position: absolute;
    left: 104px;
    width: 802px;
    height: 458px;
    overflow: hidden;
    box-shadow: 10px 12px 22px rgba(0,0,0,0.28);
  }
  .card--front { top: 87px; background: var(--white); }
  .card--back  { top: 603px; background: var(--green); }

  .front__bar { position: absolute; left: 0; top: 0; width: 29px; height: 100%; background: var(--charcoal); }
  .front__panel { position: absolute; inset: 0; }

  .holder-name {
    position: absolute; left: 54px; top: 118px;
    font-family: "Montserrat", sans-serif; font-weight: 800;
    font-size: 48px; letter-spacing: 1px; color: var(--charcoal); line-height: 1;
  }
  .holder-rule { position: absolute; left: 50px; top: 175px; width: 364px; height: 3px; background: var(--green); }

  .contacts { position: absolute; left: 54px; top: 274px; list-style: none; }
  .contacts__item {
    display: flex; align-items: center; height: 39.5px;
    font-family: "Fira Sans", sans-serif; font-size: 22px; color: var(--ink);
  }
  .contacts__icon { width: 28px; height: 28px; margin-right: 17px; flex: none; }

  .brand {
    position: absolute; font-family: "Fira Sans", sans-serif; font-weight: 600;
    color: var(--white); text-align: center; line-height: 1;
  }
  .brand--front { left: 548px; top: 112px; width: 200px; font-size: 33px; }
  .brand--back { left: 0; right: 0; top: 196px; font-size: 76px; }

  .services {
    position: absolute; left: 532px; top: 205px; list-style: none;
    font-family: "Fira Sans", sans-serif; font-size: 22px; line-height: 28px; color: var(--white);
  }
  .services__item { position: relative; padding-left: 20px; }
  .services__item::before {
    content: ""; position: absolute; left: 2px; top: 10px;
    width: 8px; height: 8px; border-radius: 50%; background: var(--white);
  }
</style>
</head>
<body>
<div class="canvas">

  <section class="card card--front">
    <svg class="front__panel" width="802" height="458" viewBox="0 0 802 458" aria-hidden="true">
      <polygon points="561,0 802,0 802,458 408,458" fill="var(--green)"/>
    </svg>
    <div class="front__bar"></div>

    <h1 class="holder-name">DANA CREWE</h1>
    <div class="holder-rule"></div>

    <ul class="contacts">
      <li class="contacts__item">
        <svg class="contacts__icon" viewBox="0 0 28 28" aria-hidden="true">
          <circle cx="14" cy="14" r="14" fill="var(--green)"/>
          <path d="M14 6.5a5.5 5.5 0 0 0-5.5 5.5c0 4 5.5 9.5 5.5 9.5s5.5-5.5 5.5-9.5A5.5 5.5 0 0 0 14 6.5z" fill="#fff"/>
          <circle cx="14" cy="12" r="2.2" fill="var(--green)"/>
        </svg>
        Torvale Plumbing Canberra
      </li>
      <li class="contacts__item">
        <svg class="contacts__icon" viewBox="0 0 28 28" aria-hidden="true">
          <circle cx="14" cy="14" r="14" fill="var(--green)"/>
          <path d="M9.5 7.5l3 3-1.6 1.8c.9 1.9 2.4 3.4 4.3 4.3l1.8-1.6 3 3-2 2c-5.5-.6-10-5.1-10.5-10.5z" fill="#fff"/>
          <path d="M15.5 8.5a4 4 0 0 1 4 4M15.5 5.8a6.7 6.7 0 0 1 6.7 6.7" stroke="#fff" stroke-width="1.4" fill="none" stroke-linecap="round"/>
        </svg>
        0400 555 018
      </li>
      <li class="contacts__item">
        <svg class="contacts__icon" viewBox="0 0 28 28" aria-hidden="true">
          <circle cx="14" cy="14" r="14" fill="var(--green)"/>
          <rect x="7.5" y="9.5" width="13" height="9" rx="1" fill="#fff"/>
          <path d="M7.8 10l6.2 4.6 6.2-4.6" stroke="var(--green)" stroke-width="1.3" fill="none"/>
        </svg>
        info@torvaleworks.com
      </li>
      <li class="contacts__item">
        <svg class="contacts__icon" viewBox="0 0 28 28" aria-hidden="true">
          <circle cx="14" cy="14" r="14" fill="var(--green)"/>
          <circle cx="14" cy="14" r="6.5" fill="none" stroke="#fff" stroke-width="1.4"/>
          <ellipse cx="14" cy="14" rx="2.8" ry="6.5" fill="none" stroke="#fff" stroke-width="1.2"/>
          <path d="M7.5 14h13M8.5 10.8h11M8.5 17.2h11" stroke="#fff" stroke-width="1.1"/>
        </svg>
        torvaleworks.com.au
      </li>
    </ul>

    <div class="brand brand--front">Torvale Works</div>

    <ul class="services">
      <li class="services__item">Bathroom/Kitchen<br>Renovations</li>
      <li class="services__item">Drainage</li>
      <li class="services__item">PlumbingMaintenance</li>
      <li class="services__item">Stormwater</li>
      <li class="services__item">Water Leaks</li>
      <li class="services__item">Water Tanks and<br>Septics</li>
    </ul>
  </section>

  <section class="card card--back">
    <div class="brand brand--back">Torvale Works</div>
  </section>

</div>
</body>
</html>
```